Visit Qalimora Card (School That only teach arabic language) (Guaranteed Payment)

Hi, we are a new school That Teach arabic language in Tunisia, we are looking to conceptulize visit cards for our team. The business card will be printed in color and on Both Sides. We want to communiquer: innovation, excellence, professionalism, leadership and trust. Would we need the business card at the end with the details of everyone of our team (3) General and aussi has one for our center in Tunis. La même designed is used througout of course. Waiting for your sugestions! The address is the Sámi for all the visit cards: 47 Rue des Oliviers Zembra Cedar Building, 3rd Floor 4071 Jardins de Sidra 2, Tunisia aussi la même is the website for all www.qalimora.example The 4 visits Card Those names are: Karim Ouertani Jonas Freiberg Rania Gharbi Qalimora For Karim's Ouertani Visit Card Function name: Managing Partner Phone number: 216 94120386 Email: karim.ouertani@qalimora. example For Rania's visit card function name: Marketing Assistant Phone number: 216 97402615 Email: rania.gharbi@qalimora.example For Jonas's visit card: Function name: Managing Partner Phone number: 49 151 08246519 Mail: @ jonas.freiberg qalimora.example You can find our logo in the attachment.

```html
<!DOCTYPE html>
<html lang="en">
<head>
<meta charset="utf-8">
<title>Qalimora Business Card</title>
<link rel="stylesheet" href="https://fonts.googleapis.com/css2?family=Open+Sans:wght@400;600;700&display=swap">
<style>
  :root {
    --brand-blue: #0c5394;
    --card-white: #ffffff;
    --page-bg: #e9ebee;
    --text-light: #ffffff;
    --divider: rgba(255, 255, 255, 0.45);
  }
  * { box-sizing: border-box; margin: 0; padding: 0; }
  html, body {
    width: 1200px;
    height: 900px;
    overflow: hidden;
    background: var(--page-bg);
    font-family: "Open Sans", Arial, sans-serif;
  }
  .canvas {
    position: relative;
    width: 1200px;
    height: 900px;
  }
  .card {
    position: absolute;
    left: 300px;
    width: 600px;
    height: 340px;
    overflow: hidden;
    box-shadow: 0 6px 18px rgba(0, 0, 0, 0.18);
  }
  .card-front {
    top: 90px;
    background: var(--brand-blue);
    color: var(--text-light);
  }
  .card-back {
    top: 470px;
    background: var(--card-white);
  }
  .wordmark {
    display: flex;
    align-items: center;
    gap: 14px;
    font-weight: 600;
    font-size: 58px;
    letter-spacing: 1px;
    line-height: 1;
  }
  .wordmark-square {
    width: 26px;
    height: 26px;
  }
  .card-front .wordmark {
    position: absolute;
    top: 118px;
    left: 0;
    right: 0;
    justify-content: center;
    color: var(--text-light);
  }
  .card-front .wordmark-square { background: var(--text-light); }
  .website {
    position: absolute;
    top: 212px;
    left: 0;
    right: 0;
    text-align: center;
    font-size: 13px;
    letter-spacing: 0.3px;
  }
  .card-back .wordmark {
    position: absolute;
    top: 70px;
    left: 0;
    right: 0;
    justify-content: center;
    color: var(--brand-blue);
  }
  .card-back .wordmark-square { background: var(--brand-blue); }
  .details-band {
    position: absolute;
    left: 0;
    right: 0;
    bottom: 0;
    height: 148px;
    background: var(--brand-blue);
    color: var(--text-light);
  }
  .person {
    position: absolute;
    top: 14px;
    right: 282px;
    text-align: right;
  }
  .person-name {
    font-size: 17px;
    font-weight: 700;
  }
  .person-role {
    font-size: 13px;
    margin-top: 1px;
  }
  .contact-line {
    display: flex;
    align-items: center;
    justify-content: flex-end;
    gap: 6px;
    font-size: 14px;
  }
  .contact-phone { margin-top: 12px; }
  .contact-email { margin-top: 4px; }
  .contact-icon { width: 11px; height: 11px; flex: none; }
  .column-divider {
    position: absolute;
    top: 14px;
    left: 330px;
    width: 1px;
    height: 100px;
    background: var(--divider);
  }
  .address {
    position: absolute;
    top: 12px;
    left: 342px;
    font-size: 12.5px;
    line-height: 1.45;
    font-style: normal;
  }
</style>
</head>
<body>
<main class="canvas">
  <section class="card card-front" aria-label="Card front">
    <div class="wordmark"><span class="wordmark-square"></span><span>qalimora</span></div>
    <p class="website">www.qalimora.example</p>
  </section>

  <section class="card card-back" aria-label="Card back">
    <div class="wordmark"><span class="wordmark-square"></span><span>qalimora</span></div>
    <div class="details-band">
      <div class="person">
        <p class="person-name">Karim's Ouertani</p>
        <p class="person-role">Managing Partner</p>
        <p class="contact-line contact-phone">
          <span>216 94120386</span>
          <svg class="contact-icon" viewBox="0 0 12 12" aria-hidden="true">
            <path d="M1 4.5 Q6 1 11 4.5 L9.5 6 L8 5 L8 4 Q6 3.3 4 4 L4 5 L2.5 6 Z M3 7 H9 L10 11 H2 Z" fill="#ffffff"/>
          </svg>
        </p>
        <p class="contact-line contact-email">
          <span>karim.ouertani@qalimora.example</span>
          <svg class="contact-icon" viewBox="0 0 12 12" aria-hidden="true">
            <rect x="0.5" y="2.5" width="11" height="7.5" fill="#ffffff"/>
            <path d="M0.5 2.5 L6 7 L11.5 2.5" fill="none" stroke="#0c5394" stroke-width="1"/>
          </svg>
        </p>
      </div>
      <span class="column-divider"></span>
      <address class="address">
        47 Rue des Oliviers<br>
        Zembra Cedar Building, 3rd Floor<br>
        4071 Jardins de Sidra 2, Tunisia
      </address>
    </div>
  </section>
</main>
</body>
</html>
```